Business Card Design (NEW FILES)

ATTENTION: New vector files are available. Please update your design to reflect/use the new (better resolution) logo images.

Seeking a unique and professional business card design for a commercial drone photography/videography business. The layout should feature
the logo (attached) and include the following information:
Pete Varner
978-552-6170
www.skylarkvisuals.example
NVR Certified Remote Pilot

Pete Varner

```html
<!DOCTYPE html>
<html lang="en">
<head>
<meta charset="utf-8">
<title>Skylark Visuals – Business Card</title>
<link href="https://fonts.googleapis.com/css2?family=Montserrat:wght@400;500;700&family=Open+Sans:wght@400&display=swap" rel="stylesheet">
<style>
  :root {
    --bg: #d6d6d6;
    --paper: #f1f1f1;
    --navy: #14163a;
    --orange: #d9712f;
    --ink: #1d1d1d;
  }
  * { box-sizing: border-box; margin: 0; padding: 0; }
  html, body { width: 1200px; height: 1051px; overflow: hidden; }
  body {
    background: var(--bg);
    position: relative;
    font-family: "Open Sans", sans-serif;
    color: var(--ink);
  }
  .card {
    position: absolute;
    width: 525px;
    height: 300px;
    background: var(--paper);
    border-bottom: 6px solid var(--orange);
    border-right: 6px solid var(--orange);
    box-shadow: 0 18px 40px rgba(0,0,0,0.25);
  }
  .card--brand { left: 600px; top: 210px; }
  .card--contact { left: 75px; top: 540px; }

  .wordmark {
    font-family: "Montserrat", sans-serif;
    font-weight: 500;
    color: var(--navy);
    display: flex;
    align-items: center;
    white-space: nowrap;
  }
  .wordmark__dot {
    border-radius: 50%;
    background: var(--orange);
    flex: none;
  }
  .card--brand .wordmark {
    position: absolute; left: 0; right: 0; top: 0; bottom: 0;
    justify-content: center; font-size: 40px; letter-spacing: 1px; gap: 16px;
  }
  .card--brand .wordmark__dot { width: 22px; height: 22px; }

  .card--contact .wordmark {
    position: absolute; left: 34px; top: 92px;
    font-size: 21px; gap: 9px;
  }
  .card--contact .wordmark__dot { width: 12px; height: 12px; }

  .divider {
    position: absolute; left: 282px; top: 70px;
    width: 1.5px; height: 110px; background: var(--orange);
  }
  .contact { position: absolute; left: 306px; top: 72px; }
  .contact__name {
    font-family: "Montserrat", sans-serif; font-weight: 700;
    color: var(--orange); font-size: 21px; line-height: 1.1;
  }
  .contact__role {
    font-family: "Montserrat", sans-serif; font-weight: 400;
    font-size: 13px; margin-bottom: 16px;
  }
  .contact__line {
    display: flex; align-items: center; gap: 7px;
    font-size: 13px; line-height: 20px;
  }
  .contact__line svg { width: 11px; height: 11px; flex: none; }
  .credential {
    position: absolute; left: 0; right: 0; bottom: 30px;
    text-align: center; font-size: 14px;
  }
</style>
</head>
<body>
  <section class="card card--brand" aria-label="Business card front">
    <div class="wordmark"><span class="wordmark__dot"></span>Skylark Visuals</div>
  </section>

  <section class="card card--contact" aria-label="Business card back">
    <div class="wordmark"><span class="wordmark__dot"></span>Skylark Visuals</div>
    <div class="divider"></div>
    <div class="contact">
      <p class="contact__name">Pete Varner</p>
      <p class="contact__role">Owner</p>
      <p class="contact__line">
        <svg viewBox="0 0 24 24" aria-hidden="true"><path fill="#d9712f" d="M6.6 10.8a15.1 15.1 0 0 0 6.6 6.6l2.2-2.2a1 1 0 0 1 1-.25 11.4 11.4 0 0 0 3.6.57 1 1 0 0 1 1 1V20a1 1 0 0 1-1 1A17 17 0 0 1 3 4a1 1 0 0 1 1-1h3.5a1 1 0 0 1 1 1c0 1.25.2 2.45.57 3.57a1 1 0 0 1-.25 1z"/></svg>
        978-552-6170
      </p>
      <p class="contact__line">
        <svg viewBox="0 0 24 24" aria-hidden="true"><circle cx="12" cy="12" r="10" fill="none" stroke="#d9712f" stroke-width="3"/><path d="M2 12h20M12 2c3 3 3 17 0 20M12 2c-3 3-3 17 0 20" fill="none" stroke="#d9712f" stroke-width="2"/></svg>
        www.skylarkvisuals.example
      </p>
    </div>
    <p class="credential">NVR Certified Remote Pilot Fully Insured</p>
  </section>
</body>
</html>
```